Dental Medical History Form - Content provided

Design a medical history form for a dental practice. Content is provided so all that is needed is the formatting to make it look great and easy to read.

"Patient Information" to include all information contained in top portion of the "Patient Medical History Form" docx file.

"Medical History" should follow the formatting and content of the "Exact Medical History" file as this is what the entry fields look like in our practice software and so we would like it to match.

1st page - Patient info, allergies, medications, antibiotics, joint replacement, pregnancy.

2nd page - Do you have, or have you had, any of the following? . . . . . . .
Updates

Project Deadline Extended Reason: Picked too short of a deadline to start (2 days) Added Monday, February 13, 2017

Target Market(s)

All ages but must be clear enough for elderly to read. Use as much space as possible to keep font size bigger yet keep to two pages

Industry/Entity Type

Dental

Font styles to use
Sans Serif

Requirements
Must have
• All content provided
• Our logo at the top (file provided)
• Century Gothic Font
• Limit to two pages

```html
<!DOCTYPE html>
<html lang="en">
<head>
<meta charset="utf-8">
<title>Medical History Form – Lumen Dental</title>
<link rel="stylesheet" href="https://fonts.googleapis.com/css2?family=Questrial&display=swap">
<style>
  :root {
    --ink: #2f2f2f;
    --heading: #4a4a4a;
    --muted: #5e5e5e;
    --box: #a9a9a9;
    --rule: #9a9a9a;
    --paper: #ffffff;
  }
  * { box-sizing: border-box; margin: 0; padding: 0; }
  html, body { width: 851px; height: 1200px; overflow: hidden; background: var(--paper); }
  body { font-family: "Questrial", "Century Gothic", sans-serif; color: var(--ink); }
  .page { position: relative; width: 851px; height: 1200px; }

  .brand { position: absolute; right: 42px; top: 66px; display: flex; align-items: center; gap: 10px; color: var(--muted); }
  .brand-dot { width: 12px; height: 12px; border-radius: 50%; background: var(--muted); }
  .brand-name { font-size: 26px; line-height: 1; }

  .form-title { position: absolute; left: 54px; top: 144px; font-size: 17px; font-weight: bold; color: var(--heading); letter-spacing: 0.2px; }

  .group-title { position: absolute; font-size: 15.5px; color: var(--heading); font-weight: bold; letter-spacing: 0.2px; }
  .left { left: 55px; }
  .right { left: 472px; }

  .rows { position: absolute; list-style: none; }
  .rows li { display: flex; align-items: center; height: 20.3px; font-size: 16px; white-space: nowrap; }
  .rows .label { width: 273px; }
  .rows.right .label { width: 236px; }
  .rows .label.tight { font-size: 15.4px; letter-spacing: -0.5px; }
  .opt { display: inline-flex; align-items: center; font-size: 14.5px; }
  .opt.yes { width: 54px; }
  .box { display: inline-block; width: 12px; height: 12px; border: 1px solid var(--box); margin-left: 4px; }

  .line-field { position: absolute; display: flex; align-items: flex-end; font-size: 16px; }
  .line-field .fill { border-bottom: 1px solid var(--rule); margin-left: 2px; height: 15px; }
  .line-field.heading { color: var(--heading); font-weight: bold; font-size: 15.5px; }

  .closing { position: absolute; left: 0; width: 851px; top: 1124px; text-align: center; font-size: 12.3px; line-height: 14.6px; color: var(--ink); }
</style>
</head>
<body>
<main class="page">
  <header class="brand">
    <span class="brand-dot"></span>
    <span class="brand-name">Lumen Dental</span>
  </header>

  <h1 class="form-title">Do you have, or have you had any of the following?</h1>

  <h2 class="group-title left" style="top:176px">Dental</h2>
  <ul class="rows left" style="left:55px;top:198px">
    <li><span class="label">Acid Reflux</span><span class="opt yes">yes<i class="box"></i></span><span class="opt">no<i class="box"></i></span></li>
    <li><span class="label">Bad Breath/Taste</span><span class="opt yes">yes<i class="box"></i></span><span class="opt">no<i class="box"></i></span></li>
    <li><span class="label">Bleeding/Swollen/Sore Gums</span><span class="opt yes">yes<i class="box"></i></span><span class="opt">no<i class="box"></i></span></li>
    <li><span class="label">Blisters/Ulcers in Mouth</span><span class="opt yes">yes<i class="box"></i></span><span class="opt">no<i class="box"></i></span></li>
    <li><span class="label">Broken Tooth/filling</span><span class="opt yes">yes<i class="box"></i></span><span class="opt">no<i class="box"></i></span></li>
    <li><span class="label">Burning Tongue</span><span class="opt yes">yes<i class="box"></i></span><span class="opt">no<i class="box"></i></span></li>
    <li><span class="label">Dry mouth</span><span class="opt yes">yes<i class="box"></i></span><span class="opt">no<i class="box"></i></span></li>
    <li><span class="label">Food collection between teeth</span><span class="opt yes">yes<i class="box"></i></span><span class="opt">no<i class="box"></i></span></li>
    <li><span class="label">Grinding/clenching teeth (day/night)</span><span class="opt yes">yes<i class="box"></i></span><span class="opt">no<i class="box"></i></span></li>
    <li><span class="label">Loose teeth</span><span class="opt yes">yes<i class="box"></i></span><span class="opt">no<i class="box"></i></span></li>
    <li><span class="label">Crooked teeth</span><span class="opt yes">yes<i class="box"></i></span><span class="opt">no<i class="box"></i></span></li>
    <li><span class="label">Discoloured teeth</span><span class="opt yes">yes<i class="box"></i></span><span class="opt">no<i class="box"></i></span></li>
    <li><span class="label">Sensitivity to Hot/Cold</span><span class="opt yes">yes<i class="box"></i></span><span class="opt">no<i class="box"></i></span></li>
    <li><span class="label">Tooth pain when chewing</span><span class="opt yes">yes<i class="box"></i></span><span class="opt">no<i class="box"></i></span></li>
    <li><span class="label">Jaw pain/Fracture</span><span class="opt yes">yes<i class="box"></i></span><span class="opt">no<i class="box"></i></span></li>
    <li><span class="label">Orthodontic treatment/history</span><span class="opt yes">yes<i class="box"></i></span><span class="opt">no<i class="box"></i></span></li>
    <li><span class="label">Oral Cancer</span><span class="opt yes">yes<i class="box"></i></span><span class="opt">no<i class="box"></i></span></li>
  </ul>

  <h2 class="group-title left" style="top:573px">Diet/Lifestyle</h2>
  <ul class="rows left" style="left:55px;top:598px">
    <li><span class="label tight">Drink more than one glass alcohol per day</span><span class="opt yes">yes<i class="box"></i></span><span class="opt">no<i class="box"></i></span></li>
    <li><span class="label">Smoking</span><span class="opt yes">yes<i class="box"></i></span><span class="opt">no<i class="box"></i></span></li>
    <li><span class="label">Carbonated drinks</span><span class="opt yes">yes<i class="box"></i></span><span class="opt">no<i class="box"></i></span></li>
    <li><span class="label">Sugary foods</span><span class="opt yes">yes<i class="box"></i></span><span class="opt">no<i class="box"></i></span></li>
  </ul>

  <h2 class="group-title left" style="top:708px">Blood</h2>
  <ul class="rows left" style="left:55px;top:733px">
    <li><span class="label">Anaemia</span><span class="opt yes">yes<i class="box"></i></span><span class="opt">no<i class="box"></i></span></li>
    <li><span class="label">Blood clots</span><span class="opt yes">yes<i class="box"></i></span><span class="opt">no<i class="box"></i></span></li>
    <li><span class="label">Leukemia</span><span class="opt yes">yes<i class="box"></i></span><span class="opt">no<i class="box"></i></span></li>
    <li><span class="label">Low platelets</span><span class="opt yes">yes<i class="box"></i></span><span class="opt">no<i class="box"></i></span></li>
    <li><span class="label">Lymphoma</span><span class="opt yes">yes<i class="box"></i></span><span class="opt">no<i class="box"></i></span></li>
    <li><span class="label">Haemophelia</span><span class="opt yes">yes<i class="box"></i></span><span class="opt">no<i class="box"></i></span></li>
  </ul>

  <h2 class="group-title left" style="top:876px;left:54px">Infectious Disease</h2>
  <ul class="rows left" style="left:54px;top:901px">
    <li><span class="label">Creutzfeldt-Jakob Disease</span><span class="opt yes">yes<i class="box"></i></span><span class="opt">no<i class="box"></i></span></li>
    <li><span class="label">Hepatitis A,B,C,D</span><span class="opt yes">yes<i class="box"></i></span><span class="opt">no<i class="box"></i></span></li>
    <li><span class="label">HIV/AIDS</span><span class="opt yes">yes<i class="box"></i></span><span class="opt">no<i class="box"></i></span></li>
    <li><span class="label">Influenza</span><span class="opt yes">yes<i class="box"></i></span><span class="opt">no<i class="box"></i></span></li>
    <li><span class="label">Shingles</span><span class="opt yes">yes<i class="box"></i></span><span class="opt">no<i class="box"></i></span></li>
    <li><span class="label">Tuberculosis</span><span class="opt yes">yes<i class="box"></i></span><span class="opt">no<i class="box"></i></span></li>
  </ul>

  <h2 class="group-title right" style="top:176px">Chest</h2>
  <ul class="rows right" style="left:471px;top:201px">
    <li><span class="label">Bronchitis</span><span class="opt yes">yes<i class="box"></i></span><span class="opt">no<i class="box"></i></span></li>
    <li><span class="label">Cystic Fibrosis</span><span class="opt yes">yes<i class="box"></i></span><span class="opt">no<i class="box"></i></span></li>
    <li><span class="label">Emphysema</span><span class="opt yes">yes<i class="box"></i></span><span class="opt">no<i class="box"></i></span></li>
    <li><span class="label">Pneumonia</span><span class="opt yes">yes<i class="box"></i></span><span class="opt">no<i class="box"></i></span></li>
  </ul>

  <h2 class="group-title right" style="top:305px;left:471px">Heart</h2>
  <ul class="rows right" style="left:472px;top:330px">
    <li><span class="label">Angina</span><span class="opt yes">yes<i class="box"></i></span><span class="opt">no<i class="box"></i></span></li>
    <li><span class="label">Atrial Fibrillation</span><span class="opt yes">yes<i class="box"></i></span><span class="opt">no<i class="box"></i></span></li>
    <li><span class="label">Blood Pressure (High/Low)</span><span class="opt yes">yes<i class="box"></i></span><span class="opt">no<i class="box"></i></span></li>
    <li><span class="label">Congenital Heart Disease</span><span class="opt yes">yes<i class="box"></i></span><span class="opt">no<i class="box"></i></span></li>
    <li><span class="label">Heart attack</span><span class="opt yes">yes<i class="box"></i></span><span class="opt">no<i class="box"></i></span></li>
    <li><span class="label">Heart murmur</span><span class="opt yes">yes<i class="box"></i></span><span class="opt">no<i class="box"></i></span></li>
    <li><span class="label">Heart surgery</span><span class="opt yes">yes<i class="box"></i></span><span class="opt">no<i class="box"></i></span></li>
    <li><span class="label">Heart valve replacement</span><span class="opt yes">yes<i class="box"></i></span><span class="opt">no<i class="box"></i></span></li>
    <li><span class="label">Infective endocarditis</span><span class="opt yes">yes<i class="box"></i></span><span class="opt">no<i class="box"></i></span></li>
    <li><span class="label">Rheumatic Heart Disease</span><span class="opt yes">yes<i class="box"></i></span><span class="opt">no<i class="box"></i></span></li>
    <li><span class="label">Pacemaker</span><span class="opt yes">yes<i class="box"></i></span><span class="opt">no<i class="box"></i></span></li>
    <li><span class="label">Stent</span><span class="opt yes">yes<i class="box"></i></span><span class="opt">no<i class="box"></i></span></li>
  </ul>

  <h2 class="group-title right" style="top:603px">Other</h2>
  <ul class="rows right" style="left:472px;top:630px">
    <li><span class="label">Anxiety/PTSD</span><span class="opt yes">yes<i class="box"></i></span><span class="opt">no<i class="box"></i></span></li>
    <li><span class="label">Arthritis</span><span class="opt yes">yes<i class="box"></i></span><span class="opt">no<i class="box"></i></span></li>
    <li><span class="label">Alzheimer’s</span><span class="opt yes">yes<i class="box"></i></span><span class="opt">no<i class="box"></i></span></li>
    <li><span class="label">Asthma</span><span class="opt yes">yes<i class="box"></i></span><span class="opt">no<i class="box"></i></span></li>
    <li><span class="label">Anaphylaxis</span><span class="opt yes">yes<i class="box"></i></span><span class="opt">no<i class="box"></i></span></li>
    <li><span class="label">Auto-immune disease</span><span class="opt yes">yes<i class="box"></i></span><span class="opt">no<i class="box"></i></span></li>
    <li><span class="label">Coeliac</span><span class="opt yes">yes<i class="box"></i></span><span class="opt">no<i class="box"></i></span></li>
    <li><span class="label">Depression</span><span class="opt yes">yes<i class="box"></i></span><span class="opt">no<i class="box"></i></span></li>
    <li><span class="label">Diabetes</span><span class="opt yes">yes<i class="box"></i></span><span class="opt">no<i class="box"></i></span></li>
    <li><span class="label">Epilepsy</span><span class="opt yes">yes<i class="box"></i></span><span class="opt">no<i class="box"></i></span></li>
    <li><span class="label">Kidney Disease</span><span class="opt yes">yes<i class="box"></i></span><span class="opt">no<i class="box"></i></span></li>
    <li><span class="label">Liver Disease</span><span class="opt yes">yes<i class="box"></i></span><span class="opt">no<i class="box"></i></span></li>
    <li><span class="label">Osteoporosis</span><span class="opt yes">yes<i class="box"></i></span><span class="opt">no<i class="box"></i></span></li>
    <li><span class="label">Parkinson’s</span><span class="opt yes">yes<i class="box"></i></span><span class="opt">no<i class="box"></i></span></li>
    <li><span class="label">Radiation to Head/Neck</span><span class="opt yes">yes<i class="box"></i></span><span class="opt">no<i class="box"></i></span></li>
    <li><span class="label">Schizophrenia</span><span class="opt yes">yes<i class="box"></i></span><span class="opt">no<i class="box"></i></span></li>
    <li><span class="label">Snoring</span><span class="opt yes">yes<i class="box"></i></span><span class="opt">no<i class="box"></i></span></li>
    <li><span class="label">Sleep apnea</span><span class="opt yes">yes<i class="box"></i></span><span class="opt">no<i class="box"></i></span></li>
    <li><span class="label">Stroke</span><span class="opt yes">yes<i class="box"></i></span><span class="opt">no<i class="box"></i></span></li>
  </ul>

  <div class="line-field" style="left:472px;top:1032px">Other:<span class="fill" style="width:296px"></span></div>

  <div class="line-field heading" style="left:53px;top:1087px">Signature:<span class="fill" style="width:338px"></span></div>
  <div class="line-field heading" style="left:556px;top:1087px">Date:<span class="fill" style="width:212px"></span></div>

  <footer class="closing">
    Thank you for the time to complete your medical history form.<br>
    Oral health is linked to overall health and this comprehensive questionnaire<br>
    will help us to provide you with optimal and safe care.
  </footer>
</main>
</body>
</html>
```